TrellanVita Website - Biologics storage and handling

I would like a beginning design on a website for TrellanVita:

A Boston-based company dedicated to sourcing, storing, and supplying biologic materials of all kinds to the life sciences and scientific markets. From starting reagents, to basic and intermediate materials, to final synthesized and engineered products, we provide value throughout the biologics supply chain. TrellanVita provides backup, overflow, emergency, and stocking storage solutions to companies on a temporary or permanent basis. Life sciences companies can take advantage of the fact that the company is located in the middle of the Boston/Cambridge biotechnology corridor in order to have quick and efficient access to their cold chain materials. Out of state companies can leverage TrellanVita’s location for efficient distribution of materials to partner and client organizations. We also provide other value added services to organizations that do not have the local manpower, such as sourcing, supply, and distribution of materials.

The design should be mostly a white background with clean, linear, geometric colors added in according to the blue and orange color scheme represented in the corporate logo attached.

The website needs to communicate reliable service and provide the concept of a company dedicated to handling and providing client biological samples in a secure and efficient manner.

Some local competitors are:
1. Korbel BioWorks: www.korbelbw.example
2. LabVault: www.labvault-store.example

From a design perspective, I like the Halvenor Thera website:

www.halvenorthera.example

Target Market(s)

Life sciences companies and other organizations

Industry/Entity Type

Biotechnology

Coding

Coded - Design and coding required

Number of Pages Required

5+ page

Font styles to use
Sans Serif

Colors
3176b5
0455a3
f37122

Requirements
Must have
• Tabs for pages:
About - Company information.
Platform - Inventory and sample management cloud platform; temperature profiling, logging, and reporting.
Services - Refrigeration and freezing services for biological samples, logistics services, sourcing services, courier services.
Updates - News, events, blog.
Login portal - Entry point for getting into platform. Maybe some freemium content here.
Nice to have
• Please be creative about website page sections, vibrant colors according to my established color scheme, and clean, linear, geometric shapes. I would like a white background with nice colors, clean lines and borders, and a very contemporary look. I want o
Should not have
• This is not a Business to Consumer business. This is a Business to Business enterprise. There should not be consumer oriented language. It is more about service and relationship management.

```html
<!DOCTYPE html>
<html lang="en">
<head>
<meta charset="utf-8">
<title>TrellanVita — Biologics Storage and Handling</title>
<link rel="stylesheet" href="https://fonts.googleapis.com/css2?family=Open+Sans:wght@400;600;700&family=Raleway:wght@300;400;600&display=swap">
<style>
:root{
  --blue:#3176b5;
  --blue-deep:#0455a3;
  --navy:#0b3a78;
  --orange:#f37122;
  --ink:#2c3440;
  --muted:#6b7280;
  --line:#e3e6ea;
  --footer:#2b2b2b;
  --footer-dark:#1f1f1f;
  --white:#fff;
}
*{box-sizing:border-box;margin:0;padding:0}
html,body{width:1200px;height:3616px;overflow:hidden}
body{font-family:"Open Sans",Arial,sans-serif;color:var(--ink);background:var(--white);font-size:14px}
a{color:inherit;text-decoration:none}
.section-title{font-family:"Raleway",Arial,sans-serif;font-weight:400;font-size:44px;letter-spacing:2px;text-align:center;text-transform:uppercase}
.section-title .accent{color:var(--orange)}
.btn{display:inline-block;background:var(--orange);color:#fff;font-size:13px;font-weight:600;text-transform:uppercase;padding:12px 26px;border-radius:3px;letter-spacing:.5px}
.btn-outline{display:inline-block;border:1px solid var(--orange);color:var(--ink);font-size:12px;font-weight:600;text-transform:uppercase;padding:9px 18px;border-radius:2px}

/* header */
.site-header{height:144px;position:relative;padding:0 60px}
.brand{position:absolute;left:60px;top:22px;display:flex;flex-direction:column;align-items:center;gap:8px}
.brand-mark{width:54px;height:54px;border:4px solid var(--navy)}
.brand-name{font-family:"Raleway",Arial,sans-serif;font-weight:600;font-size:28px;color:var(--navy);letter-spacing:1px;text-transform:uppercase}
.utility{position:absolute;right:60px;top:24px;display:flex;gap:30px;font-size:13px;font-weight:600;color:var(--orange)}
.utility span{display:flex;align-items:center;gap:8px}
.utility i{width:22px;height:22px;border-radius:50%;background:var(--orange);display:inline-flex;align-items:center;justify-content:center}
.main-nav{position:absolute;right:60px;top:92px;display:flex;gap:40px;font-size:13px;font-weight:600;text-transform:uppercase;color:var(--ink)}
.main-nav a.active{color:var(--orange);border-bottom:2px solid var(--orange);padding-bottom:6px}

/* hero */
.hero{position:relative;height:716px;overflow:hidden}
.hero-photo{position:absolute;inset:0;background:linear-gradient(100deg,#5b7488 0%,#8fa6b8 35%,#c9d5de 60%,#9eb1bf 100%)}
.hero-copy{position:absolute;left:110px;top:210px;color:#fff;width:520px}
.hero-copy h1{font-family:"Raleway",Arial,sans-serif;font-weight:400;font-size:68px;letter-spacing:3px;text-transform:uppercase;margin-bottom:22px}
.hero-copy p{font-size:15px;line-height:1.6;margin-bottom:28px}
.hero-cut{position:absolute;left:0;bottom:0;width:1200px;height:90px}

/* about */
.about{padding:86px 120px 0;text-align:center;height:548px}
.about .section-title{margin-bottom:10px}
.title-rule{width:60px;height:2px;background:var(--orange);margin:0 auto 46px}
.about p{font-size:13px;line-height:1.85;color:var(--muted);text-align:left;margin-bottom:22px}
.about .btn{margin-top:12px}

/* platform */
.platform{height:380px;padding-top:10px}
.platform .section-title{color:var(--orange);margin-bottom:30px}
.platform-grid{display:flex;gap:26px;justify-content:center}
.platform-card{width:250px;height:224px;border:2px solid #bcd0e6;display:flex;flex-direction:column;align-items:center;justify-content:center;gap:18px;background:linear-gradient(180deg,#fff,#f6f8fb)}
.platform-card.warm{border-color:#f7c7a6}
.platform-card h3{font-size:14px;font-weight:600;color:var(--blue-deep);text-align:center;line-height:1.5;padding:0 20px}
.platform-card.warm h3{color:var(--orange)}

/* services */
.services{height:520px;background:linear-gradient(160deg,var(--blue-deep) 0%,var(--blue) 55%,#1d5fa6 100%);color:#fff;padding-top:68px}
.services .section-title{color:#fff;margin-bottom:10px}
.services .title-rule{background:#fff;margin-bottom:56px}
.service-grid{display:flex;justify-content:center;gap:60px}
.service{width:220px;text-align:center}
.service-icon{width:112px;height:112px;border:2px solid #fff;border-radius:50%;margin:0 auto 22px;display:flex;align-items:center;justify-content:center}
.service h3{font-size:15px;font-weight:700;text-transform:uppercase;line-height:1.4;margin-bottom:12px}
.service p{font-size:12px;line-height:1.6;color:#dce8f5}

/* blog */
.blog{height:768px;padding-top:60px}
.blog .section-title{margin-bottom:44px}
.blog-grid{display:flex;justify-content:center;gap:30px}
.post{width:310px;height:456px;box-shadow:0 3px 14px rgba(0,0,0,.12);text-align:center}
.post-photo{height:232px}
.post-photo.p1{background:linear-gradient(135deg,#d0dbe6,#8aa3bd 60%,#c43f3a)}
.post-photo.p2{background:linear-gradient(135deg,#e7eef5,#9db7d4 50%,#4f79ad)}
.post-photo.p3{background:linear-gradient(135deg,#cfe4f3,#5aa9dc 55%,#1f5c93)}
.post h3{font-size:18px;font-weight:600;text-transform:uppercase;margin:22px 0 6px}
.post .date{color:var(--orange);font-weight:700;font-size:15px;margin-bottom:14px}
.post p{font-size:12px;line-height:1.6;color:var(--muted);padding:0 30px;margin-bottom:22px}

/* newsletter */
.newsletter{height:272px;background:linear-gradient(90deg,#e2611a,var(--orange) 50%,#e8661d);color:#fff;text-align:center;padding-top:44px}
.newsletter .section-title{color:#fff;font-size:38px;margin-bottom:14px}
.newsletter p{font-size:12px;line-height:1.6;width:620px;margin:0 auto 22px;color:#ffe6d6}
.news-input{width:460px;height:40px;margin:0 auto 16px;border:1px solid #fff;text-align:left;padding:11px 16px;font-size:12px;color:#ffe6d6}
.news-submit{display:inline-block;background:var(--blue-deep);color:#fff;font-weight:700;font-size:13px;padding:10px 34px;text-transform:uppercase}

/* footer */
.site-footer{height:340px;background:var(--footer);color:#d9d9d9;position:relative}
.footer-brand{position:absolute;left:110px;top:110px;display:flex;flex-direction:column;align-items:center;gap:12px}
.footer-brand .brand-mark{border-color:#fff;width:70px;height:70px}
.footer-brand .brand-name{color:#fff;font-size:36px}
.footer-col{position:absolute;top:50px}
.footer-col h4{font-size:16px;font-weight:600;color:#fff;text-transform:uppercase;letter-spacing:1px;margin-bottom:20px}
.links{left:450px}
.links li{list-style:none;font-size:11px;text-transform:uppercase;margin-bottom:10px;display:flex;align-items:center;gap:10px}
.links li::before{content:"";width:5px;height:5px;background:var(--orange)}
.contact{left:640px}
.contact li,.follow li{list-style:none;font-size:12px;display:flex;align-items:center;gap:12px;margin-bottom:16px;line-height:1.4}
.contact i,.follow i{width:24px;height:24px;border-radius:50%;background:#555;flex:none}
.follow{left:920px}
.follow i{background:#4a4a4a;width:28px;height:28px}
.copyright{height:56px;background:var(--footer-dark);color:#aaa;font-size:12px;text-align:center;line-height:56px}
</style>
</head>
<body>

<header class="site-header">
  <a class="brand" href="#">
    <span class="brand-mark"></span>
    <span class="brand-name">TrellanVita</span>
  </a>
  <div class="utility">
    <span><i><svg width="12" height="12" viewBox="0 0 12 12"><circle cx="6" cy="4" r="2.5" fill="#fff"/><path d="M1.5 11c0-3 2-4.5 4.5-4.5s4.5 1.5 4.5 4.5z" fill="#fff"/></svg></i>LOGIN</span>
    <span><i><svg width="12" height="12" viewBox="0 0 12 12"><path d="M2.5 1l2 2.5-1 1.3c.7 1.4 1.7 2.4 3.1 3.1l1.3-1 2.6 2-1.1 1.8C5 10.5 1.5 7 .9 2.1z" fill="#fff"/></svg></i>CALL US: (617) 555-0142</span>
  </div>
  <nav class="main-nav">
    <a class="active" href="#">Home</a>
    <a href="#">About</a>
    <a href="#">Platform</a>
    <a href="#">Services</a>
    <a href="#">News</a>
    <a href="#">Contact</a>
  </nav>
</header>

<section class="hero">
  <div class="hero-photo" role="img" aria-label="Gloved hand opening a laboratory cold storage freezer door"></div>
  <div class="hero-copy">
    <h1>TrellanVita</h1>
    <p>Secure cold chain storage and supply of biologic materials for life science organizations across the Boston biotech corridor.</p>
    <a class="btn" href="#">Read More</a>
  </div>
  <svg class="hero-cut" viewBox="0 0 1200 90" preserveAspectRatio="none"><polygon points="0,20 600,90 1200,20 1200,90 0,90" fill="#fff"/></svg>
</section>

<section class="about">
  <h2 class="section-title">About <span class="accent">TrellanVita</span></h2>
  <div class="title-rule"></div>
  <p>A Boston-based company dedicated to sourcing, storing, and supplying biologic materials of all kinds to the life sciences and scientific markets. From starting reagents, to basic and intermediate materials, to final synthesized and engineered products, we provide value throughout the biologics supply chain. TrellanVita provides backup, overflow, emergency, and stocking storage solutions to companies on a temporary or permanent basis.</p>
  <p>Life sciences companies can take advantage of the fact that the company is located in the middle of the Boston/Cambridge biotechnology corridor in order to have quick and efficient access to their cold chain materials.</p>
  <a class="btn" href="#">Read More</a>
</section>

<section class="platform">
  <h2 class="section-title">Platform</h2>
  <div class="platform-grid">
    <div class="platform-card">
      <svg width="70" height="60" viewBox="0 0 70 60" fill="none" stroke="#0455a3" stroke-width="2.5"><path d="M18 40a11 11 0 0 1 2-22 15 15 0 0 1 28 2 10 10 0 0 1 4 20z"/><path d="M26 40v12M35 40v14M44 40v12"/><circle cx="26" cy="54" r="2"/><circle cx="44" cy="54" r="2"/></svg>
      <h3>Inventory and sample management cloud platform</h3>
    </div>
    <div class="platform-card warm">
      <svg width="40" height="64" viewBox="0 0 40 64" fill="none" stroke="#f37122" stroke-width="2.5"><path d="M14 8a6 6 0 0 1 12 0v32a11 11 0 1 1-12 0z"/><circle cx="20" cy="49" r="5" fill="#f37122"/><path d="M20 44V18"/></svg>
      <h3>Temperature Profiling</h3>
    </div>
    <div class="platform-card">
      <svg width="56" height="62" viewBox="0 0 56 62" fill="none" stroke="#0455a3" stroke-width="2.5"><rect x="6" y="4" width="44" height="54" rx="3"/><rect x="16" y="14" width="24" height="20"/><path d="M16 42h24M16 49h16"/></svg>
      <h3>Logging</h3>
    </div>
    <div class="platform-card warm">
      <svg width="64" height="60" viewBox="0 0 64 60" fill="none" stroke="#f37122" stroke-width="2.5"><path d="M6 56h54"/><rect x="10" y="38" width="8" height="18" fill="#f37122"/><rect x="24" y="30" width="8" height="26" fill="#f37122"/><rect x="38" y="22" width="8" height="34" fill="#f37122"/><path d="M8 28l16-12 12 8 20-18"/><path d="M48 6h8v8"/></svg>
      <h3>Reporting</h3>
    </div>
  </div>
</section>

<section class="services">
  <h2 class="section-title">Our Services</h2>
  <div class="title-rule"></div>
  <div class="service-grid">
    <div class="service">
      <div class="service-icon"><svg width="54" height="54" viewBox="0 0 54 54" fill="none" stroke="#fff" stroke-width="2.5"><path d="M27 3v48M6 15l42 24M6 39l42-24"/><path d="M21 7l6 5 6-5M21 47l6-5 6 5"/></svg></div>
      <h3>Refrigeration &amp; Freezing</h3>
      <p>Validated cold storage for biologic samples with continuous monitoring.</p>
    </div>
    <div class="service">
      <div class="service-icon"><svg width="58" height="44" viewBox="0 0 58 44" fill="none" stroke="#fff" stroke-width="2.5"><rect x="2" y="6" width="34" height="26"/><path d="M36 14h12l8 10v8H36"/><circle cx="14" cy="36" r="5"/><circle cx="44" cy="36" r="5"/></svg></div>
      <h3>Logistics Services</h3>
      <p>Coordinated cold chain transfer to partner and client organizations.</p>
    </div>
    <div class="service">
      <div class="service-icon"><svg width="54" height="54" viewBox="0 0 54 54" fill="none" stroke="#fff" stroke-width="2.5"><circle cx="30" cy="18" r="12"/><path d="M30 11v14M26 14h7a2.5 2.5 0 0 1 0 5h-6a2.5 2.5 0 0 0 0 5h7"/><path d="M4 40h10l8 4h14l12-8-4-3-10 5H24"/></svg></div>
      <h3>Sourcing Services</h3>
      <p>Procurement of reagents and materials from qualified suppliers.</p>
    </div>
    <div class="service">
      <div class="service-icon"><svg width="54" height="50" viewBox="0 0 54 50" fill="none" stroke="#fff" stroke-width="2.5"><rect x="6" y="12" width="42" height="32"/><path d="M6 12l21 16 21-16"/><path d="M18 4h18"/></svg></div>
      <h3>Courier Services</h3>
      <p>Same-day local delivery across the Boston and Cambridge region.</p>
    </div>
  </div>
</section>

<section class="blog">
  <h2 class="section-title">Latest <span class="accent">Blog</span></h2>
  <div class="blog-grid">
    <article class="post">
      <div class="post-photo p1" role="img" aria-label="Gloved hand holding a sample tube in a laboratory"></div>
      <h3>Sed ut perspicia</h3>
      <div class="date">08 June 2020</div>
      <p>Nemo enim ipsam voluptatem quia voluptas sit aspernatur aut odit aut fugit sed consequuntur.</p>
      <a class="btn-outline" href="#">Read More</a>
    </article>
    <article class="post">
      <div class="post-photo p2" role="img" aria-label="Rows of labelled sample vials in a rack"></div>
      <h3>Sed ut perspicia</h3>
      <div class="date">08 June 2020</div>
      <p>Nemo enim ipsam voluptatem quia voluptas sit aspernatur aut odit aut fugit sed consequuntur.</p>
      <a class="btn-outline" href="#">Read More</a>
    </article>
    <article class="post">
      <div class="post-photo p3" role="img" aria-label="Blue liquid samples being pipetted into test tubes"></div>
      <h3>Sed ut perspicia</h3>
      <div class="date">08 June 2020</div>
      <p>Nemo enim ipsam voluptatem quia voluptas sit aspernatur aut odit aut fugit sed consequuntur.</p>
      <a class="btn-outline" href="#">Read More</a>
    </article>
  </div>
</section>

<section class="newsletter">
  <h2 class="section-title">Newsletter Signup</h2>
  <p>Sed ut perspiciatis unde omnis iste natus error sit voluptatem accusantium doloremque laudantium totam rem aperiam eaque ipsa quae ab illo inventore veritatis et quasi.</p>
  <div class="news-input">Enter Your Email</div>
  <a class="news-submit" href="#">Submit</a>
</section>

<footer class="site-footer">
  <div class="footer-brand">
    <span class="brand-mark"></span>
    <span class="brand-name">TrellanVita</span>
  </div>
  <div class="footer-col links">
    <h4>Quick Links</h4>
    <ul><li>Home</li><li>About Us</li><li>Platform</li><li>Services</li><li>News</li><li>Contact Us</li></ul>
  </div>
  <div class="footer-col contact">
    <h4>Contact Us</h4>
    <ul>
      <li><i></i>(617) 555-0142</li>
      <li><i></i>info@trellanvita.example</li>
      <li><i></i>9764 Lorem Ipsum Dummy text<br>Lorem ipsum dummy</li>
    </ul>
  </div>
  <div class="footer-col follow">
    <h4>Follow Us</h4>
    <ul>
      <li><i></i>Like us on<br>our page</li>
      <li><i></i>Follow us<br>for updates</li>
      <li><i></i>Connect with<br>our team</li>
    </ul>
  </div>
</footer>
<div class="copyright">© Copyrights 2020 TrellanVita All Rights Reserved.</div>

</body>
</html>
```